Web Design Project - vR Advise

We want to modernise our web page profile. We have an existing web site that we are particularly not proud of (www.vradvise.com.au).
We have started to build a new web site using Plivex and we like the structure of it, but we need it to be professionally designed and implemented.

This current development site can be viewed here: dev.vradvise.com.au

We would like a complete design for the entire website, ready for deployment.

(We still need to finalise the content, as we have just developed new products that we hope to launch in August both on this web site and by a Vendor Forum.)
Updates

Reason: Project must be complete by this friday at the latest.

Target Market(s)

Larger companies where the robustness of their IT infrastructure is critical. Our tools and services provide for monitoring of every device

Industry/Entity Type

Build

Requirements
Must have
• Responsive design for different screen sizes.

BrightDock help desk software integrated with the website.
Currently can be viewed at support.vradvise.com.au
Brightdock only supports custom css.

Nice to have
• Customer experience testimonials in a rotating banner
Chirply and Pagebook links in the footer
We use Avenir as a company font.
Use company colours as in the logo (green and blue)

```html
<!DOCTYPE html>
<html lang="en">
<head>
<meta charset="utf-8">
<title>vR Advise</title>
<link rel="stylesheet" href="https://fonts.googleapis.com/css2?family=Open+Sans:wdth,wght@75..100,300..800&display=swap">
<style>
:root{
  --green:#5cb82e;
  --green-dark:#3f8f1c;
  --blue:#1c8fb0;
  --teal:#1a93a6;
  --teal-dark:#0f5f6e;
  --cyan:#4fe3f0;
  --ink:#2d2d2d;
  --grey:#777;
  --light:#f7f7f7;
  --mist:#e8e8e8;
  --footer:#2f303b;
  --white:#fff;
}
*{margin:0;padding:0;box-sizing:border-box}
html,body{width:1200px;height:2448px;overflow:hidden;background:var(--white)}
body{font-family:"Open Sans",Arial,sans-serif;color:var(--ink);position:relative}
section,header,footer{position:absolute;left:0;width:1200px}
.abs{position:absolute}

/* header */
.site-header{top:0;height:80px;background:var(--white)}
.brand{left:180px;top:18px;display:flex;align-items:center;gap:10px;font-size:24px;font-weight:700;color:var(--blue)}
.brand-dot{width:34px;height:34px;border-radius:50%;background:var(--green)}
.main-nav{right:170px;top:34px;display:flex;gap:28px;font-size:13px;font-weight:700;color:#555;letter-spacing:.3px}

/* hero */
.hero{top:80px;height:448px;background:radial-gradient(ellipse at 30% 40%,#6a5646 0%,#3b2e25 45%,#1d1714 100%)}
.hero-photo{left:720px;top:50px;width:260px;height:398px;border-radius:40px 40px 0 0;background:linear-gradient(160deg,#c89a7c,#8a6350 60%,#4a3a30)}
.hero-title{left:174px;top:88px;font-size:40px;line-height:44px;font-weight:800;font-stretch:80%;color:var(--white);letter-spacing:.5px}
.hero-text{left:174px;top:192px;width:320px;font-size:14px;line-height:22px;color:#eee}
.btn-hero{left:176px;top:266px;width:244px;height:54px;border-radius:4px;background:linear-gradient(#7fcf3a,#4ea51f);border:2px solid #8ed94f;color:var(--white);font-size:17px;font-weight:600;display:flex;align-items:center;justify-content:center}
.slider-arrow{width:56px;height:56px;border-radius:50%;background:rgba(40,40,40,.75);display:flex;align-items:center;justify-content:center}
.hero .prev{left:42px;top:194px}
.hero .next{left:1100px;top:194px}

/* section titles */
.section-title{left:0;width:1200px;text-align:center;font-size:28px;font-weight:400;color:var(--ink)}
.section-title .name{color:var(--green);font-weight:600}

/* services */
.services{top:528px;height:412px;background:var(--light)}
.service{width:320px;text-align:center;top:130px}
.service svg{display:block;margin:0 auto}
.service h3{margin-top:14px;font-size:18px;font-weight:400}
.service h3 span{color:var(--blue)}
.service p{margin:20px auto 0;width:300px;font-size:11px;line-height:16px;color:var(--grey)}

/* products */
.products{top:940px;height:596px;background:linear-gradient(#1b9ab0,#147f92)}
.products .section-title{color:var(--white)}
.products .section-title .name{color:var(--white);font-weight:600}
.product{width:400px;height:170px}
.product svg{position:absolute;left:0;top:0}
.product .hex-label{position:absolute;left:0;top:24px;width:78px;text-align:center;color:var(--white);font-size:24px;font-weight:600}
.product h4{position:absolute;left:100px;top:4px;font-size:15px;font-weight:600;color:var(--white)}
.product p{position:absolute;left:100px;top:28px;width:300px;font-size:13px;line-height:19px;color:#e6f6f9}
.btn-small{position:absolute;left:100px;top:120px;width:82px;height:22px;background:var(--cyan);color:var(--teal-dark);font-size:11px;display:flex;align-items:center;justify-content:center}

/* support */
.support{top:1536px;height:370px;background:var(--white)}
.support-item{width:280px;text-align:center;top:110px}
.support-art{width:200px;height:160px;margin:0 auto;border-radius:12px;background:linear-gradient(#eef3f8,#dde7ef)}
.support-item h3{margin-top:30px;font-size:16px;font-weight:600}

/* testimonials */
.testimonials{top:1906px;height:356px;background:var(--mist)}
.testimonials .section-title{font-weight:400}
.testimonials .section-title b{font-weight:700}
.quote-card{width:406px;height:116px;background:var(--white);border-radius:4px;box-shadow:0 1px 3px rgba(0,0,0,.1);top:130px}
.quote-card::after{content:"";position:absolute;left:22px;bottom:-14px;border:14px solid transparent;border-bottom:0;border-top-color:var(--white)}
.quote-mark{position:absolute;left:12px;top:2px;font-size:44px;color:#ccc;font-family:Georgia,serif}
.quote-card p{position:absolute;left:44px;top:14px;width:346px;font-size:11.5px;line-height:18px;color:#555}
.author{top:280px;display:flex;gap:12px;align-items:center}
.avatar{width:50px;height:50px;border-radius:50%;background:linear-gradient(#d8c2ad,#a48670);border:2px solid var(--white)}
.author .who{font-size:11.5px;line-height:20px;color:#666}
.author .who span{color:var(--blue)}
.ring{width:46px;height:46px;border-radius:50%;border:2px solid #bbb;background:rgba(255,255,255,.3);display:flex;align-items:center;justify-content:center;top:174px}

/* footer */
.site-footer{top:2262px;height:186px;background:var(--footer)}
.social{left:518px;top:18px;display:flex;gap:8px}
.social span{width:22px;height:22px;border-radius:50%;background:#35a7dc}
.footer-nav{left:0;width:1200px;top:112px;display:flex;justify-content:center;gap:24px;font-size:11px;color:#cfd0d6}
.copyright{left:0;width:1200px;top:150px;text-align:center;font-size:10px;color:#a3a4ad;letter-spacing:.4px}
</style>
</head>
<body>

<header class="site-header">
  <div class="brand abs"><span class="brand-dot"></span>vR Advise</div>
  <nav class="main-nav abs"><span>HOME</span><span>SERVICES</span><span>PRODUCTS</span><span>ABOUT US</span><span>CONTACT</span></nav>
</header>

<section class="hero">
  <div class="hero-photo abs" role="img" aria-label="Hand holding a smartphone showing a colourful app screen"></div>
  <h1 class="hero-title abs">ANY DEVICE, ANY<br>PLATORM, ANYWHERE</h1>
  <p class="hero-text abs">Cross-Domain, performance and services and level monitoring and management</p>
  <div class="btn-hero abs">Learn More</div>
  <div class="slider-arrow prev abs"><svg width="14" height="18"><path d="M11 2 4 9l7 7" stroke="#fff" stroke-width="3" fill="none"/></svg></div>
  <div class="slider-arrow next abs"><svg width="14" height="18"><path d="M3 2l7 7-7 7" stroke="#fff" stroke-width="3" fill="none"/></svg></div>
</section>

<section class="services">
  <h2 class="section-title abs" style="top:56px"><span class="name">vR Advise</span> SERVICES</h2>

  <div class="service abs" style="left:140px">
    <svg width="96" height="108" viewBox="0 0 96 108"><polygon points="48,2 94,28 94,80 48,106 2,80 2,28" fill="var(--green)"/><text x="48" y="68" text-anchor="middle" font-size="40" fill="#fff" font-family="Arial,sans-serif">⌘</text></svg>
    <h3>Consulting <span>SERVICES</span></h3>
    <p>Leveraging architectural and consulting skills to develop a technology agnostic end-state, supported by vR Advise Professional Services and Operational Support</p>
  </div>
  <div class="service abs" style="left:440px">
    <svg width="96" height="108" viewBox="0 0 96 108"><polygon points="48,2 94,28 94,80 48,106 2,80 2,28" fill="var(--green)"/><rect x="32" y="32" width="32" height="40" rx="5" fill="#fff"/><circle cx="48" cy="46" r="7" fill="var(--green)"/><path d="M37 68q11-16 22 0z" fill="var(--green)"/></svg>
    <h3>Professional <span>SERVICES</span></h3>
    <p>Leveraging architectural and consulting skills to develop a technology agnostic end-state, supported by vR Advise Professional Services and Operational Support</p>
  </div>
  <div class="service abs" style="left:740px">
    <svg width="96" height="108" viewBox="0 0 96 108"><polygon points="48,2 94,28 94,80 48,106 2,80 2,28" fill="var(--green)"/><polygon points="48,34 68,44 48,54 28,44" fill="#fff"/><polygon points="28,48 46,57 46,78 28,68" fill="#fff"/><polygon points="68,48 50,57 50,78 68,68" fill="#fff"/></svg>
    <h3>Productised <span>SERVICES</span></h3>
    <p>Leveraging architectural and consulting skills to develop a technology agnostic end-state, supported by vR Advise Professional Services and Operational Support</p>
  </div>
</section>

<section class="products">
  <h2 class="section-title abs" style="top:56px"><span class="name">vR Advise</span> PRODUCTS</h2>

  <div class="product abs" style="left:170px;top:142px">
    <svg width="78" height="82" viewBox="0 0 78 82"><polygon points="39,1 77,21 77,61 39,81 1,61 1,21" fill="var(--teal-dark)"/></svg>
    <div class="hex-label">vR</div>
    <h4>vR Advise Products</h4>
    <p>vR Advise developed products, complimentary solutions to our vendor products. From Pocketa applications to cross-platform integrations for our Corvane and Stratix product range.</p>
    <div class="btn-small">Learn More</div>
  </div>
  <div class="product abs" style="left:622px;top:142px">
    <svg width="78" height="82" viewBox="0 0 78 82"><polygon points="39,1 77,21 77,61 39,81 1,61 1,21" fill="var(--teal-dark)"/></svg>
    <div class="hex-label">vR</div>
    <h4>vR Advise Products</h4>
    <p>vR Advise developed products, complimentary solutions to our vendor products. From Pocketa applications to cross-platform integrations for our Corvane and Stratix product range.</p>
    <div class="btn-small">Learn More</div>
  </div>
  <div class="product abs" style="left:170px;top:356px">
    <svg width="78" height="82" viewBox="0 0 78 82"><polygon points="39,1 77,21 77,61 39,81 1,61 1,21" fill="var(--teal-dark)"/></svg>
    <div class="hex-label">vR</div>
    <h4>vR Advise Products</h4>
    <p>vR Advise developed products, complimentary solutions to our vendor products. From Pocketa applications to cross-platform integrations for our Corvane and Stratix product range.</p>
    <div class="btn-small">Learn More</div>
  </div>
  <div class="product abs" style="left:622px;top:356px">
    <svg width="78" height="82" viewBox="0 0 78 82"><polygon points="39,1 77,21 77,61 39,81 1,61 1,21" fill="var(--teal-dark)"/></svg>
    <div class="hex-label">vR</div>
    <h4>vR Advise Products</h4>
    <p>vR Advise developed products, complimentary solutions to our vendor products. From Pocketa applications to cross-platform integrations for our Corvane and Stratix product range.</p>
    <div class="btn-small">Learn More</div>
  </div>
</section>

<section class="support">
  <h2 class="section-title abs" style="top:56px"><span class="name">vR Advise</span> SUPPORT</h2>
  <div class="support-item abs" style="left:150px">
    <div class="support-art" role="img" aria-label="Illustration of a support agent with documents and a checklist"></div>
    <h3>Operational Support</h3>
  </div>
  <div class="support-item abs" style="left:448px">
    <div class="support-art" role="img" aria-label="Illustration of a team of three support staff"></div>
    <h3>Extended Support</h3>
  </div>
  <div class="support-item abs" style="left:750px">
    <div class="support-art" role="img" aria-label="Illustration of a trainer pointing at a presentation board"></div>
    <h3>Training</h3>
  </div>
</section>

<section class="testimonials">
  <h2 class="section-title abs" style="top:56px"><b>Clients</b> TESTIMONIALS</h2>
  <div class="ring abs" style="left:80px"><svg width="12" height="16"><path d="M10 2 3 8l7 6" stroke="#fff" stroke-width="2.5" fill="none"/></svg></div>
  <div class="ring abs" style="left:1074px"><svg width="12" height="16"><path d="M2 2l7 6-7 6" stroke="#fff" stroke-width="2.5" fill="none"/></svg></div>

  <div class="quote-card abs" style="left:172px">
    <span class="quote-mark">“</span>
    <p>Lorem ipsum dolor sit amet conse ectetur adip cing elit, sed do eiusmod tempor incididunt ut labore et dolore magna aliqua. Ut enim admint veniam, quis nostrud exercitation aute irure dolor in reprehe.</p>
  </div>
  <div class="quote-card abs" style="left:620px">
    <span class="quote-mark">“</span>
    <p>Lorem ipsum dolor sit amet conse ectetur adip cing elit, sed do eiusmod tempor incididunt ut labore et dolore magna aliqua. Ut enim admint veniam, quis nostrud exercitation aute irure dolor in reprehe.</p>
  </div>

  <div class="author abs" style="left:186px">
    <div class="avatar" role="img" aria-label="Portrait of client Marlon Keats"></div>
    <div class="who"><span>Marlon Keats</span> Summer '12 Cohort<br>Software Engineer at NewYork</div>
  </div>
  <div class="author abs" style="left:634px">
    <div class="avatar" role="img" aria-label="Portrait of client Tessa Nolan"></div>
    <div class="who"><span>Tessa Nolan</span> Summer '11 Cohort<br>Software Engineer at NewYork</div>
  </div>
</section>

<footer class="site-footer">
  <div class="social abs"><span></span><span></span><span></span><span></span></div>
  <nav class="footer-nav abs"><span>HOME</span><span>SERVICES</span><span>PRODUCTS</span><span>ABOUT US</span><span>CONTACT</span></nav>
  <p class="copyright abs">COPYRIGHT · 2013 vR Advise. ALL RIGHT RESERVED.</p>
</footer>

</body>
</html>
```